Small and passionate motorcycle workshop requires a business card that kicks butt!

I'm Dermot, I'm passionate about my motorcycles, I'm passionate about my desert racing and I'm a passionate motorcycle technician, that's why I started my own motorcycle workshop: 'Rivo Tarka'.
I started my workshop in my dining room and it’s eventually moved into a newly renovated shed that my Grandpa built with his own two hands in the early 1960's. To the customer the shed looks like a farm shed on my property, however the inside is ready for open heart surgery on their "Baby" which could be a late model sports bike, a highway cruiser, an old four-wheeler or an off road desert racing weapon!
This business is my own, I've built it from my dining room floor and I'm deeply passionate about it.
I need a professional business card and logo which looks like a heart and soul is intermingled through it because that is how my business is run. Rivo Tarka may have started from my dining room but it has always been professionally run and I have always put my passion into the bikes I've worked on.

-The text only logo needs to be comprised of 'Rivo Tarka'
-The business card will be double sided

And I do realise it will be a hard task to make something look professional and personal at the same time...however there are some very talented people in this world and I can’t wait to see what you create!

I've added some logo/designs that I'm fond of.

Industry/Entity Type

Racing

Requirements
Must have
• My name - Dermot Fasquell
My Qualification - Qualified Motorcycle Technician
Ph - 0487305219
Email - rivotarka@kelpmail.example
Address - 17 Bellwin Ridge Road, Marrowvale, KR
ABN - 62 918 304 217 (plesase include the 'ABN' part
Needs to include these dot points:
-Servicing
-Repairs
-All makes/models
-Weekends by appt.
-Pick-up/delivery available
Nice to have
• I like the idea of calling myself a "Qualified and Passionate Motorcycle Technician". If the card does not come across that it’s a passionate business I'd like this line to be used on the card near my name.

One idea I like would include having the text only logo on the front being quite bold and contrasted to the background, then having my name and number smaller underneath somewhere. I'm very open to whatever comes my way so I'm look forward to seeing some sweet ideas!

```html
<!DOCTYPE html>
<html lang="en">
<head>
<meta charset="utf-8">
<title>Rivo Tarka — Business Card</title>
<link rel="stylesheet" href="https://fonts.googleapis.com/css2?family=Roboto+Condensed:wght@400;700&family=Share+Tech+Mono&display=swap">
<style>
  :root {
    --backdrop: #b9b9b9;
    --paper: #ffffff;
    --charcoal: #3a3a3a;
    --charcoal-deep: #262626;
    --charcoal-soft: #4a4a4a;
    --moto-blue: #2f5cc0;
    --ink-light: #f2f2f2;
    --shadow: rgba(0, 0, 0, 0.28);
  }
  * { box-sizing: border-box; margin: 0; padding: 0; }
  html, body {
    width: 1200px;
    height: 800px;
    overflow: hidden;
    background: var(--backdrop);
  }
  .canvas {
    position: relative;
    width: 1200px;
    height: 800px;
    display: flex;
    align-items: center;
    justify-content: center;
    gap: 40px;
  }
  .card {
    position: relative;
    width: 540px;
    height: 330px;
    overflow: hidden;
    box-shadow: 0 10px 24px var(--shadow);
    font-family: "Share Tech Mono", monospace;
  }

  /* ---------- Front ---------- */
  .card-front { background: var(--paper); }
  .front-band {
    position: absolute;
    inset: 0;
    width: 540px;
    height: 330px;
  }
  .wordmark {
    font-family: "Roboto Condensed", sans-serif;
    font-weight: 700;
    text-transform: uppercase;
    line-height: 0.9;
    letter-spacing: 1px;
  }
  .front-wordmark {
    position: absolute;
    top: 36px;
    right: 40px;
    text-align: left;
    color: var(--moto-blue);
  }
  .wordmark-top { display: block; font-size: 54px; }
  .wordmark-bottom { display: block; font-size: 84px; letter-spacing: 3px; }

  .holder {
    position: absolute;
    left: 26px;
    top: 176px;
    color: var(--ink-light);
  }
  .holder-name {
    font-family: "Roboto Condensed", sans-serif;
    font-weight: 400;
    font-size: 26px;
    line-height: 1.02;
  }
  .holder-surname { text-transform: uppercase; }
  .holder-title {
    margin-top: 6px;
    font-size: 16px;
    color: var(--moto-blue);
    letter-spacing: 0.3px;
    white-space: nowrap;
  }
  .holder-phone {
    margin-top: 10px;
    font-size: 22px;
    letter-spacing: 1px;
  }

  /* ---------- Back ---------- */
  .card-back {
    background: linear-gradient(135deg, var(--charcoal-soft) 0%, var(--charcoal) 45%, var(--charcoal-deep) 100%);
    color: var(--ink-light);
  }
  .back-wordmark {
    position: absolute;
    top: 92px;
    left: 30px;
    color: var(--ink-light);
  }
  .back-wordmark .wordmark-top { font-size: 40px; }
  .back-wordmark .wordmark-bottom { font-size: 62px; letter-spacing: 2px; }

  .services {
    position: absolute;
    top: 28px;
    left: 330px;
    list-style: none;
    font-size: 12.5px;
    line-height: 1.55;
  }
  .services li { display: flex; align-items: center; gap: 9px; }
  .services svg { flex: none; }

  .contact {
    position: absolute;
    left: 30px;
    bottom: 30px;
    display: grid;
    grid-template-columns: 78px auto;
    row-gap: 3px;
    font-size: 13px;
  }
  .contact dt { color: var(--moto-blue); }
  .contact dd { color: var(--ink-light); }
</style>
</head>
<body>
<main class="canvas">

  <section class="card card-front" aria-label="Business card front">
    <svg class="front-band" viewBox="0 0 540 330" aria-hidden="true">
      <defs>
        <linearGradient id="bandShade" x1="0" y1="0" x2="1" y2="1">
          <stop offset="0" stop-color="#454545"/>
          <stop offset="1" stop-color="#252525"/>
        </linearGradient>
      </defs>
      <path d="M0 168 H176 Q186 168 191 177 L198 192 Q203 202 214 202 H540 V330 H0 Z" fill="url(#bandShade)"/>
      <path d="M0 168 H176 Q186 168 191 177 L198 192 Q203 202 214 202 H540" fill="none" stroke="var(--moto-blue)" stroke-width="3"/>
    </svg>

    <h1 class="wordmark front-wordmark">
      <span class="wordmark-top">Rivo</span>
      <span class="wordmark-bottom">Tarka</span>
    </h1>

    <div class="holder">
      <p class="holder-name">Dermot<br><span class="holder-surname">Fasquell</span></p>
      <p class="holder-title">Qualified and Passionate Motorcycle Technician</p>
      <p class="holder-phone">0487305219</p>
    </div>
  </section>

  <section class="card card-back" aria-label="Business card back">
    <ul class="services">
      <li><svg width="9" height="7" viewBox="0 0 9 7"><path d="M0 0 H9 L4.5 7 Z" fill="var(--moto-blue)"/></svg>Servicing</li>
      <li><svg width="9" height="7" viewBox="0 0 9 7"><path d="M0 0 H9 L4.5 7 Z" fill="var(--moto-blue)"/></svg>Repairs</li>
      <li><svg width="9" height="7" viewBox="0 0 9 7"><path d="M0 0 H9 L4.5 7 Z" fill="var(--moto-blue)"/></svg>All makes/models</li>
      <li><svg width="9" height="7" viewBox="0 0 9 7"><path d="M0 0 H9 L4.5 7 Z" fill="var(--moto-blue)"/></svg>Weekends by appt.</li>
      <li><svg width="9" height="7" viewBox="0 0 9 7"><path d="M0 0 H9 L4.5 7 Z" fill="var(--moto-blue)"/></svg>Pick-up/delivery available</li>
    </ul>

    <h2 class="wordmark back-wordmark">
      <span class="wordmark-top">Rivo</span>
      <span class="wordmark-bottom">Tarka</span>
    </h2>

    <dl class="contact">
      <dt>Email</dt><dd>rivotarka@kelpmail.example</dd>
      <dt>Address</dt><dd>17 Bellwin Ridge Road, Marrowvale, KR</dd>
      <dt>ABN</dt><dd>62 918 304 217</dd>
    </dl>
  </section>

</main>
</body>
</html>
```